Fire Risk Assessment App needs a sleek UI design

I need a sleek, modern but professional design for my 5 page Fire Risk Assessment App. Include gradient background, fire themed colours including reds, yellows, light orange and a touch of black. Design must ooze simplicity and professionalism. This is for the UK market. See attached images and word doc for more information.

Target Market(s)

General public and business owners

Industry/Entity Type

Technology / Fire Safety

Colors
00AB8E
00BBA5
67D7C9
C6EFE9
E9F9F6
59FF00
82FF00
B8FF75
E3FFCB
F4FFEA
FFC000
F8CF3A
FAE287
FDF2CF
FEFAEE
F0912C
F2A743
F7CA91
FBE8D2
FDF5EE
EE7325
F08F49
F5BC92
FAE3D3
FDF4ED
EB3D1F
EC4F4E
F09395
F8D3D4
FCEDEE

```html
<!DOCTYPE html>
<html lang="en">
<head>
<meta charset="utf-8">
<title>Fire Risk Assessment App – UI Screens</title>
<link href="https://fonts.googleapis.com/css2?family=Poppins:wght@400;500;600;700&family=Lexend:wght@400&display=swap" rel="stylesheet">
<style>
:root{
  --board:#5c3f34;
  --label:#d9c3b6;
  --cream:#fdf5ee;
  --white:#ffffff;
  --ink:#1d1d1f;
  --muted:#8a8580;
  --red:#eb3d1f;
  --red-dark:#c9291d;
  --orange:#ee7325;
  --orange-2:#f0912c;
  --amber:#ffc000;
  --green:#1fae3c;
  --line:#eadfd6;
  --soft-red:#fcedee;
}
*{box-sizing:border-box;margin:0;padding:0}
html,body{width:1200px;height:1200px;overflow:hidden;background:var(--board);font-family:'Poppins',sans-serif;color:var(--ink)}
.board{position:absolute;left:0;top:0;width:1932px;height:1932px;transform:scale(0.62112);transform-origin:0 0}
.screen-label{position:absolute;writing-mode:vertical-rl;transform:rotate(180deg);font-size:9px;letter-spacing:5.5px;color:var(--label);font-weight:500;white-space:nowrap}
.screen{position:absolute;width:205px;height:445px;border-radius:24px;overflow:hidden;background:var(--cream)}
.screen.tall{height:692px}
.screen.fire{background:linear-gradient(170deg,#f7b733 0%,#f08a2c 35%,#ea5a2b 70%,#d3302c 100%);color:var(--white)}
.status{position:absolute;top:12px;left:0;right:0;height:12px;font-size:8.5px;font-weight:600}
.status .time{position:absolute;left:26px}
.status .icons{position:absolute;right:18px;top:1px;display:flex;gap:3px;align-items:center}
.status .icons span{display:block;background:currentColor;border-radius:1px}
.home-bar{position:absolute;bottom:7px;left:50%;width:76px;height:3px;margin-left:-38px;border-radius:2px;background:var(--ink)}
.fire .home-bar{background:var(--white)}
.brand{display:flex;align-items:center;gap:6px;font-weight:600}
.brand .dot{border-radius:50%;background:var(--white)}
.flame-glow{position:absolute;left:-10px;right:-10px;bottom:0;height:220px;background:radial-gradient(ellipse at 50% 80%,rgba(255,255,255,.16),rgba(255,255,255,0) 65%)}
.foot-note{position:absolute;bottom:26px;left:0;right:0;text-align:center;font-size:5.6px;opacity:.9}
.abs{position:absolute}
.hdr{position:absolute;top:36px;left:14px;right:14px;display:flex;align-items:center;gap:6px;font-size:10px;font-weight:600}
.hdr .ic{width:13px;height:13px;border-radius:50%;background:var(--red)}
.sub{position:absolute;left:14px;font-size:6.4px;font-weight:500}
.btn{position:absolute;height:22px;border-radius:12px;display:flex;align-items:center;justify-content:center;gap:5px;font-size:6.6px;font-weight:600}
.btn.primary{background:linear-gradient(90deg,var(--orange),var(--red));color:var(--white)}
.btn.ghost{border:1px solid var(--red);color:var(--red);background:var(--white)}
.btn.light{background:var(--white);color:var(--red)}
.btn.sun{background:linear-gradient(90deg,var(--amber),var(--orange-2));color:var(--white)}
.tabbar{position:absolute;left:0;right:0;bottom:0;height:42px;background:linear-gradient(90deg,var(--red-dark),var(--red));display:flex;justify-content:space-around;padding-top:6px}
.tab{width:30px;display:flex;flex-direction:column;align-items:center;gap:3px;font-size:3.8px;color:#ffd9cf}
.tab i{display:block;width:8px;height:8px;border:1.2px solid #ffe3da;border-radius:2px}
.tab.on{color:var(--white);font-weight:600}
.tab.on i{background:var(--white)}
.tab.centre i{width:11px;height:11px;border:none;border-radius:50%;background:var(--amber)}
.card{position:absolute;background:var(--white);border-radius:6px;box-shadow:0 1px 4px rgba(120,70,40,.08)}
.row-item{position:absolute;left:14px;right:14px;height:34px;background:var(--white);border-radius:4px;display:flex;align-items:center;padding:0 8px;gap:8px}
.thumb{width:18px;height:14px;border-radius:3px;background:linear-gradient(135deg,#f4c6a8,#c9d7e3)}
.row-item .t{font-size:5.6px;font-weight:600;line-height:1.3}
.row-item .t small{display:block;font-size:4.4px;color:var(--muted);font-weight:400}
.tick-ring{margin-left:auto;width:13px;height:13px;border-radius:50%;border:1.3px solid var(--green);display:flex;align-items:center;justify-content:center}
.section-title{position:absolute;left:14px;font-size:7.6px;font-weight:600}
.option{position:absolute;left:10px;right:10px;height:36px;background:var(--white);border-radius:5px;border:1px solid #f4e7dd;display:flex;align-items:center;padding:0 9px;gap:8px}
.option.sel{border-color:var(--red)}
.radio{width:9px;height:9px;border-radius:50%;border:1px solid var(--red);flex:none}
.option.sel .radio{background:radial-gradient(circle,var(--red) 40%,transparent 45%)}
.option .name{font-size:6.4px;font-weight:600;line-height:1.35}
.option .name small{display:block;font-size:4.6px;font-weight:400;color:#555}
.option .price{margin-left:auto;text-align:right;font-size:6.6px;font-weight:600;color:var(--red);line-height:1.3}
.option .price s{display:block;font-size:5.4px;color:#555;font-weight:500}
.prop-img{flex:none;width:20px;height:16px;border-radius:3px}
.prop-img.res{background:linear-gradient(135deg,#f0a27a,#e4c9b5)}
.prop-img.com{background:linear-gradient(135deg,#cfe2e7,#9fc2b7)}
.tile{position:absolute;top:94px;width:88px;height:96px;background:var(--white);border-radius:5px;border:1px solid #f2e5db;text-align:center;font-size:6px}
.tile.sel{border-color:var(--red);color:var(--red);font-weight:600}
.tile .pic{width:40px;height:36px;margin:16px auto 14px;border-radius:5px}
.check-badge{position:absolute;top:4px;right:5px;width:9px;height:9px;border-radius:50%;background:var(--red)}
.q-head{position:absolute;left:0;right:0;top:0;height:104px;background:var(--cream)}
.q-body{position:absolute;left:0;right:0;top:104px;bottom:0;background:var(--white)}
.q-kicker{position:absolute;left:12px;top:34px;font-size:4.8px;font-weight:600}
.q-title{position:absolute;left:12px;top:42px;font-size:12px;font-weight:700}
.q-section{position:absolute;left:12px;top:62px;font-size:6.6px}
.q-section b{font-weight:600}
.save{position:absolute;right:10px;top:34px;width:38px;text-align:center;font-size:4.6px;font-weight:500}
.save i{display:block;width:18px;height:18px;margin:0 auto 4px;border-radius:50%;border:1.2px solid var(--red);background:var(--white)}
.topic-ring{position:absolute;left:84px;top:90px;width:37px;height:37px;border-radius:50%;background:var(--white);display:flex;align-items:center;justify-content:center}
.topic{position:absolute;left:0;right:0;top:135px;text-align:center;font-size:6.6px;font-weight:600}
.topic small{display:block;font-size:5.4px;font-weight:400;color:var(--muted);margin-top:2px}
.divider{position:absolute;left:12px;right:12px;top:163px;height:1px;background:var(--line)}
.q-no{position:absolute;left:12px;top:180px;font-size:5px;font-weight:600;color:var(--red)}
.q-text{position:absolute;left:12px;right:10px;top:191px;font-size:9.2px;font-weight:500;line-height:1.45}
.answers{position:absolute;left:12px;right:12px;top:238px;display:flex;justify-content:space-between;padding:0 14px}
.ans{width:24px;text-align:center;font-size:5px}
.ans i{display:flex;align-items:center;justify-content:center;width:20px;height:20px;margin:0 auto 5px;border-radius:50%;border:1.3px solid}
.ans.yes i{border-color:var(--green)}
.ans.no i,.ans.na i{border-color:var(--red)}
.ans.yes.on i{background:var(--green)}
.ans.no.on i{background:var(--red)}
.ans.yes.on{color:var(--green);font-weight:600}
.ans.no.on{color:var(--red);font-weight:600}
.note{position:absolute;left:10px;right:10px;top:290px;height:20px;border:1px solid var(--line);border-radius:4px;font-size:4.8px;padding:7px 8px;font-weight:500}
.more-label{position:absolute;left:12px;font-size:4.4px;color:var(--muted);font-weight:500}
.tool{position:absolute;height:17px;border-radius:4px;background:var(--soft-red);display:flex;align-items:center;gap:6px;padding:0 9px;font-size:5.6px}
.progress{position:absolute;left:12px;right:12px;font-size:3.8px;font-weight:600}
.progress .bar{margin-top:4px;height:3px;border-radius:2px;background:#e7e7e7}
.progress .bar span{display:block;width:60%;height:100%;border-radius:2px;background:var(--green)}
.progress .pct{position:absolute;right:0;top:0}
.photo{position:absolute;left:10px;right:10px;top:389px;height:184px;border-radius:4px;background:linear-gradient(160deg,#3a3d40,#6f7376 55%,#9a9c9c)}
.photo-del{position:absolute;right:8px;top:6px;width:10px;height:10px;border-radius:50%;background:var(--white)}
.title-mark{position:absolute;left:430px;top:1700px;width:90px;display:flex;flex-direction:column;align-items:center;gap:6px;font-family:'Lexend',sans-serif;font-size:15px;color:var(--orange-2)}
.title-mark .dot{width:58px;height:58px;border-radius:50%;background:var(--orange)}
.title-text{position:absolute;left:555px;top:1722px;font-family:'Lexend',sans-serif;font-weight:400;font-size:40px;line-height:1;color:var(--white);letter-spacing:1.2px;white-space:nowrap}
</style>
</head>
<body>
<svg width="0" height="0" style="position:absolute">
  <defs>
    <symbol id="i-tick" viewBox="0 0 10 10"><path d="M2 5.2 4.2 7.3 8 2.8" fill="none" stroke="currentColor" stroke-width="1.5" stroke-linecap="round" stroke-linejoin="round"/></symbol>
    <symbol id="i-x" viewBox="0 0 10 10"><path d="M2.5 2.5 7.5 7.5M7.5 2.5 2.5 7.5" fill="none" stroke="currentColor" stroke-width="1.4" stroke-linecap="round"/></symbol>
    <symbol id="i-ban" viewBox="0 0 10 10"><circle cx="5" cy="5" r="3.4" fill="none" stroke="currentColor" stroke-width="1.2"/><path d="M2.7 7.3 7.3 2.7" stroke="currentColor" stroke-width="1.2"/></symbol>
    <symbol id="i-bolt" viewBox="0 0 10 10"><path d="M6 .5 2 5.6h2.6L3.8 9.5 8 4.2H5.3Z" fill="currentColor"/></symbol>
    <symbol id="i-mic" viewBox="0 0 10 10"><rect x="3.5" y="1" width="3" height="5" rx="1.5" fill="currentColor"/><path d="M2.2 4.8a2.8 2.8 0 0 0 5.6 0M5 7.6v1.6" fill="none" stroke="currentColor" stroke-width=".9"/></symbol>
    <symbol id="i-cam" viewBox="0 0 10 10"><path d="M1 3h2l.8-1.2h2.4L7 3h2v5H1Z" fill="currentColor"/><circle cx="5" cy="5.4" r="1.5" fill="#fff"/></symbol>
    <symbol id="i-left" viewBox="0 0 10 10"><path d="M8 5H2M4.5 2.5 2 5l2.5 2.5" fill="none" stroke="currentColor" stroke-width="1.1" stroke-linecap="round"/></symbol>
    <symbol id="i-right" viewBox="0 0 10 10"><path d="M2 5h6M5.5 2.5 8 5 5.5 7.5" fill="none" stroke="currentColor" stroke-width="1.1" stroke-linecap="round"/></symbol>
    <symbol id="i-send" viewBox="0 0 10 10"><path d="M1 1.5 9 5 1 8.5l1.3-3.5Z" fill="currentColor"/></symbol>
    <symbol id="i-save" viewBox="0 0 10 10"><rect x="2" y="2" width="6" height="6" rx="1" fill="currentColor"/><rect x="3.5" y="2" width="3" height="2" fill="#fff"/></symbol>
    <symbol id="i-user" viewBox="0 0 10 10"><circle cx="5" cy="3.4" r="1.8" fill="currentColor"/><path d="M1.6 9a3.4 3.4 0 0 1 6.8 0Z" fill="currentColor"/></symbol>
  </defs>
</svg>

<main class="board">

  <div class="screen-label" style="left:432px;top:88px">SPLASH SCREEN</div>
  <section class="screen fire" style="left:458px;top:88px">
    <div class="status"><span class="time">9:41</span><span class="icons"><span style="width:8px;height:5px"></span><span style="width:7px;height:5px;border-radius:3px"></span><span style="width:10px;height:5px"></span></span></div>
    <div class="flame-glow" role="img" aria-label="Soft flame shapes rising from the bottom of the screen"></div>
    <div class="brand abs" style="left:0;right:0;top:92px;flex-direction:column;font-size:11px"><span class="dot" style="width:38px;height:38px"></span>Emberline</div>
    <p class="abs" style="left:0;right:0;top:172px;text-align:center;font-size:7.2px;line-height:1.6">The most user friendly<br><b style="font-size:7.6px;font-weight:600">Fire Risk Assessment App</b><br>available</p>
    <p class="foot-note">Created and endorsed by UK Fire Safety Experts</p>
    <div class="home-bar"></div>
  </section>

  <div class="screen-label" style="left:711px;top:88px">SPLASH SCREEN V2</div>
  <section class="screen fire" style="left:737px;top:88px">
    <div class="status"><span class="time">9:41</span><span class="icons"><span style="width:8px;height:5px"></span><span style="width:7px;height:5px;border-radius:3px"></span><span style="width:10px;height:5px"></span></span></div>
    <div class="flame-glow" role="img" aria-label="Soft flame shapes rising from the bottom of the screen"></div>
    <div class="brand abs" style="left:20px;top:62px;font-size:10px"><span class="dot" style="width:32px;height:32px"></span>Emberline</div>
    <p class="abs" style="left:20px;right:14px;top:153px;font-size:9.6px;line-height:1.6">The most user friendly<br><b style="font-weight:600">Fire Risk Assessment App</b><br>available</p>
    <p class="foot-note">Created and endorsed by UK Fire Safety Experts</p>
    <div class="home-bar"></div>
  </section>

  <div class="screen-label" style="left:990px;top:88px">WALKTHROUGH SCREEN</div>
  <section class="screen fire" style="left:1016px;top:88px">
    <div class="status"><span class="time">9:41</span><span class="icons"><span style="width:8px;height:5px"></span><span style="width:7px;height:5px;border-radius:3px"></span><span style="width:10px;height:5px"></span></span></div>
    <div class="brand abs" style="left:16px;top:44px;font-size:8px"><span class="dot" style="width:22px;height:22px"></span>Emberline</div>
    <div class="abs" role="img" aria-label="Illustration of an assessment question card on a phone with a hand tapping the Yes answer" style="left:22px;top:66px;width:168px;height:226px;border-radius:8px;background:linear-gradient(160deg,rgba(255,255,255,.55),rgba(255,255,255,.18))"></div>
    <div class="btn light" style="left:16px;right:16px;top:336px"><svg width="8" height="8"><use href="#i-user"/></svg>Create a free account</div>
    <div class="btn sun" style="left:16px;right:16px;top:366px"><svg width="8" height="8"><use href="#i-user"/></svg>Customer log in</div>
    <p class="foot-note">Quick tap responses and voice activated typing.</p>
    <div class="home-bar"></div>
  </section>

  <div class="screen-label" style="left:1269px;top:88px">DASHBOARD SCREEN</div>
  <section class="screen" style="left:1295px;top:88px">
    <div class="status"><span class="time">9:41</span><span class="icons"><span style="width:8px;height:5px"></span><span style="width:7px;height:5px;border-radius:3px"></span><span style="width:10px;height:5px"></span></span></div>
    <div class="hdr" style="top:35px"><span class="ic"></span>Dashboard<svg width="11" height="11" style="margin-left:auto"><circle cx="5.5" cy="5.5" r="5.5"/><use href="#i-user" x="1" y="1" width="9" height="9" style="color:#fff"/></svg></div>
    <div class="card" style="left:12px;right:12px;top:60px;height:116px">
      <span class="abs" style="left:7px;top:9px;font-size:5.6px;font-weight:500">Fire Risk Assessments</span>
      <span class="abs" style="right:7px;top:9px;font-size:4.8px;font-weight:600;color:var(--red)">VIEW ALL</span>
      <div class="abs" style="left:8px;right:8px;top:23px;height:32px;border-radius:4px;box-shadow:0 1px 4px rgba(0,0,0,.08);display:flex;align-items:center;gap:8px;padding:0 6px">
        <span class="thumb" style="width:22px;height:16px"></span>
        <span style="font-size:5.6px;font-weight:600;line-height:1.5">Hartley House<br><span style="font-size:3.8px;color:var(--orange);background:#fdecdf;padding:0 3px;border-radius:3px">● IN-PROGRESS</span></span>
        <svg width="17" height="17" viewBox="0 0 20 20" style="margin-left:auto"><circle cx="10" cy="10" r="8" fill="none" stroke="#e8e8e8" stroke-width="2"/><circle cx="10" cy="10" r="8" fill="none" stroke="#1fae3c" stroke-width="2" stroke-dasharray="37.7 50.3" transform="rotate(-90 10 10)"/><text x="10" y="11.6" font-size="4.4" text-anchor="middle" font-family="Poppins" font-weight="600">75%</text></svg>
      </div>
      <div class="abs" style="left:70px;top:66px;display:flex;gap:3px"><span style="width:9px;height:2px;background:var(--red);border-radius:1px"></span><span style="width:2px;height:2px;background:#ddd;border-radius:1px"></span><span style="width:2px;height:2px;background:#ddd;border-radius:1px"></span><span style="width:2px;height:2px;background:#ddd;border-radius:1px"></span></div>
      <div class="btn primary" style="left:7px;right:7px;top:84px;height:18px">Add new assessment</div>
    </div>
    <div class="section-title" style="left:10px;top:201px;font-size:6.8px">Completed Assessments</div>
    <div class="row-item" style="left:10px;right:10px;top:218px"><span class="thumb" style="background:linear-gradient(135deg,#cfe0e6,#a8c9bf)"></span><span class="t">Elmwood Care Home<small>18 Jul 2024</small></span><span class="tick-ring"><svg width="8" height="8" style="color:var(--green)"><use href="#i-tick"/></svg></span></div>
    <div class="row-item" style="left:10px;right:10px;top:258px"><span class="thumb"></span><span class="t">Riverside Court<small>10 Jul 2024</small></span><span class="tick-ring"><svg width="8" height="8" style="color:var(--green)"><use href="#i-tick"/></svg></span></div>
    <div class="btn ghost" style="left:53px;width:68px;top:302px;height:13px;font-size:5px">View all completed <svg width="6" height="6"><use href="#i-right"/></svg></div>
    <div class="section-title" style="left:10px;top:345px;font-size:6.8px">Purchase History</div>
    <div class="abs" style="left:10px;right:10px;top:363px;display:flex;gap:8px;align-items:center"><span class="thumb" style="width:12px;height:11px;background:linear-gradient(135deg,#d4e6e9,#b7d2c8)"></span><span style="font-size:4.8px;font-weight:600;line-height:1.4">Commercial Fire Risk Assessments<br><span style="font-weight:400;color:var(--muted);font-size:4px">Sat, 6 July 2024 • 10:48:57</span></span></div>
    <nav class="tabbar"><span class="tab on"><i></i>Dashboard</span><span class="tab"><i></i>Purchases</span><span class="tab centre"><i></i></span><span class="tab"><i></i>Support</span><span class="tab"><i></i>Logout</span></nav>
    <div class="home-bar" style="background:#fff"></div>
  </section>

  <div class="screen-label" style="left:432px;top:618px">SUPPORT SCREEN</div>
  <section class="screen" style="left:458px;top:618px">
    <div class="status"><span class="time">9:41</span><span class="icons"><span style="width:8px;height:5px"></span><span style="width:7px;height:5px;border-radius:3px"></span><span style="width:10px;height:5px"></span></span></div>
    <div class="hdr"><span class="ic"></span>Technical Support</div>
    <p class="sub" style="left:10px;top:70px">Our email support is open 24/7.</p>
    <div class="abs" style="left:0;right:0;top:88px;bottom:0;background:var(--white)">
      <span class="abs" style="left:10px;top:14px;font-size:5.4px;color:#a7a19c">Type or record your concerns here</span>
      <span class="abs" style="right:10px;top:11px;width:12px;height:12px;border-radius:50%;box-shadow:0 1px 3px rgba(0,0,0,.15);display:flex;align-items:center;justify-content:center;color:var(--red)"><svg width="7" height="7"><use href="#i-mic"/></svg></span>
    </div>
    <div class="btn primary" style="left:12px;right:12px;top:355px"><svg width="7" height="7"><use href="#i-send"/></svg>Send</div>
    <nav class="tabbar"><span class="tab"><i></i>Dashboard</span><span class="tab"><i></i>Purchases</span><span class="tab centre"><i></i></span><span class="tab on"><i></i>Support</span><span class="tab"><i></i>Logout</span></nav>
    <div class="home-bar" style="background:#fff"></div>
  </section>

  <div class="screen-label" style="left:711px;top:618px">PURCHASE OPTIONS</div>
  <section class="screen" style="left:737px;top:618px">
    <div class="status"><span class="time">9:41</span><span class="icons"><span style="width:8px;height:5px"></span><span style="width:7px;height:5px;border-radius:3px"></span><span style="width:10px;height:5px"></span></span></div>
    <div class="hdr"><span class="ic" style="border-radius:2px;height:10px"></span>Purchase Options</div>
    <p class="sub" style="left:10px;top:70px">Select Fire Risk Assessment Payment Options</p>
    <div class="option" style="top:93px"><span class="radio"></span><span class="name">Bronze<small>1 Fire Risk Assessment</small></span><span class="price">£19.99</span></div>
    <div class="option sel" style="top:136px"><span class="radio"></span><span class="name">Silver<small>3 Fire Risk Assessments</small></span><span class="price"><s>£59.97</s>£54.99</span></div>
    <div class="option" style="top:179px"><span class="radio"></span><span class="name">Gold<small>5 Fire Risk Assessments</small></span><span class="price"><s>£99.95</s>£89.99</span></div>
    <div class="option" style="top:222px"><span class="radio"></span><span class="name">Platinum<small>10 Fire Risk Assessments</small></span><span class="price"><s>£199.90</s>£174.99</span></div>
    <div class="btn primary" style="left:10px;right:10px;top:332px">Continue</div>
    <div class="btn ghost" style="left:10px;right:10px;top:362px">Cancel</div>
    <nav class="tabbar"><span class="tab"><i></i>Dashboard</span><span class="tab on"><i></i>Purchases</span><span class="tab centre"><i></i></span><span class="tab"><i></i>Support</span><span class="tab"><i></i>Logout</span></nav>
    <div class="home-bar" style="background:#fff"></div>
  </section>

  <div class="screen-label" style="left:990px;top:618px">ADD NEW ASSESSMENT V1</div>
  <section class="screen" style="left:1016px;top:618px">
    <div class="status"><span class="time">9:41</span><span class="icons"><span style="width:8px;height:5px"></span><span style="width:7px;height:5px;border-radius:3px"></span><span style="width:10px;height:5px"></span></span></div>
    <div class="hdr"><span class="ic"></span>Add Fire Risk Assessment</div>
    <p class="sub" style="left:10px;top:70px">Select type of property</p>
    <div class="option sel" style="top:93px;height:40px"><span class="radio"></span><span class="prop-img res" role="img" aria-label="Illustration of a house"></span><span class="name">Residential</span></div>
    <div class="option" style="top:139px;height:40px"><span class="radio"></span><span class="prop-img com" role="img" aria-label="Illustration of an office building"></span><span class="name">Commercial</span></div>
    <div class="btn ghost" style="left:10px;width:88px;top:392px">Cancel</div>
    <div class="btn primary" style="right:10px;width:88px;top:392px">Continue</div>
    <div class="home-bar"></div>
  </section>

  <div class="screen-label" style="left:1269px;top:618px">ADD NEW ASSESSMENT V2</div>
  <section class="screen" style="left:1295px;top:618px">
    <div class="status"><span class="time">9:41</span><span class="icons"><span style="width:8px;height:5px"></span><span style="width:7px;height:5px;border-radius:3px"></span><span style="width:10px;height:5px"></span></span></div>
    <div class="hdr"><span class="ic"></span>Add Fire Risk Assessment</div>
    <p class="sub" style="left:10px;top:70px">Select type of property</p>
    <div class="tile sel" style="left:10px"><span class="check-badge"></span><div class="pic prop-img res" role="img" aria-label="Illustration of a house"></div>Residential</div>
    <div class="tile" style="right:10px"><div class="pic prop-img com" role="img" aria-label="Illustration of an office building"></div>Commercial</div>
    <div class="btn ghost" style="left:10px;width:88px;top:392px">Cancel</div>
    <div class="btn primary" style="right:10px;width:88px;top:392px">Continue</div>
    <div class="home-bar"></div>
  </section>

  <div class="screen-label" style="left:432px;top:1148px">ADD ASSESSMENT - QUESTION</div>
  <section class="screen" style="left:458px;top:1148px">
    <div class="q-head"></div><div class="q-body"></div>
    <div class="status"><span class="time">9:41</span><span class="icons"><span style="width:8px;height:5px"></span><span style="width:7px;height:5px;border-radius:3px"></span><span style="width:10px;height:5px"></span></span></div>
    <span class="q-kicker">FIRE RISK ASSESSMENT</span><span class="q-title">Fire Hazards</span><span class="q-section"><b>Section 22.5</b> / 30.00</span>
    <span class="save"><i><svg width="9" height="9" style="color:var(--red);margin-top:3.5px"><use href="#i-save"/></svg></i>Save and close</span>
    <span class="topic-ring"><svg width="37" height="37" viewBox="0 0 40 40"><circle cx="20" cy="20" r="17" fill="none" stroke="#1fae3c" stroke-width="2.4"/><use href="#i-bolt" x="11" y="10" width="18" height="20" style="color:var(--amber)"/></svg></span>
    <p class="topic">Electronic Sources of Ignition<small>(Clause 13 &amp; Annex B)</small></p>
    <div class="divider"></div>
    <span class="q-no">QUESTION 22.05</span>
    <p class="q-text">Are reasonable measures taken to prevent fires of electrical origin?</p>
    <div class="answers"><span class="ans yes"><i><svg width="10" height="10" style="color:var(--green)"><use href="#i-tick"/></svg></i>Yes</span><span class="ans no"><i><svg width="10" height="10" style="color:var(--red)"><use href="#i-x"/></svg></i>No</span><span class="ans na"><i><svg width="11" height="11" style="color:var(--red)"><use href="#i-ban"/></svg></i>N/A</span></div>
    <span class="more-label" style="top:296px">MORE OPTIONS</span>
    <span class="tool" style="left:10px;width:90px;top:307px"><svg width="7" height="7"><use href="#i-mic"/></svg>Mic</span>
    <span class="tool" style="right:10px;width:90px;top:307px"><svg width="8" height="8"><use href="#i-cam"/></svg>Take a photo</span>
    <div class="progress" style="top:373px">ASSESSMENT PROGRESS<span class="pct">60%</span><div class="bar"><span></span></div></div>
    <div class="btn ghost" style="left:10px;width:88px;top:398px;height:20px"><svg width="7" height="7"><use href="#i-left"/></svg>Prev</div>
    <div class="btn primary" style="right:10px;width:88px;top:398px;height:20px">Next<svg width="7" height="7"><use href="#i-right"/></svg></div>
    <div class="home-bar"></div>
  </section>

  <div class="screen-label" style="left:711px;top:1148px">ADD ASSESSMENT - QUESTION - YES</div>
  <section class="screen" style="left:737px;top:1148px">
    <div class="q-head"></div><div class="q-body"></div>
    <div class="status"><span class="time">9:41</span><span class="icons"><span style="width:8px;height:5px"></span><span style="width:7px;height:5px;border-radius:3px"></span><span style="width:10px;height:5px"></span></span></div>
    <span class="q-kicker">FIRE RISK ASSESSMENT</span><span class="q-title">Fire Hazards</span><span class="q-section"><b>Section 22.5</b> / 30.00</span>
    <span class="save"><i><svg width="9" height="9" style="color:var(--red);margin-top:3.5px"><use href="#i-save"/></svg></i>Save and close</span>
    <span class="topic-ring"><svg width="37" height="37" viewBox="0 0 40 40"><circle cx="20" cy="20" r="17" fill="none" stroke="#1fae3c" stroke-width="2.4"/><use href="#i-bolt" x="11" y="10" width="18" height="20" style="color:var(--amber)"/></svg></span>
    <p class="topic">Electronic Sources of Ignition<small>(Clause 13 &amp; Annex B)</small></p>
    <div class="divider"></div>
    <span class="q-no">QUESTION 22.05</span>
    <p class="q-text">Are reasonable measures taken to prevent fires of electrical origin?</p>
    <div class="answers"><span class="ans yes on"><i><svg width="10" height="10" style="color:#fff"><use href="#i-tick"/></svg></i>Yes</span><span class="ans no"><i><svg width="10" height="10" style="color:var(--red)"><use href="#i-x"/></svg></i>No</span><span class="ans na"><i><svg width="11" height="11" style="color:var(--red)"><use href="#i-ban"/></svg></i>N/A</span></div>
    <span class="more-label" style="top:296px">MORE OPTIONS</span>
    <span class="tool" style="left:10px;width:90px;top:307px"><svg width="7" height="7"><use href="#i-mic"/></svg>Mic</span>
    <span class="tool" style="right:10px;width:90px;top:307px"><svg width="8" height="8"><use href="#i-cam"/></svg>Take a photo</span>
    <div class="progress" style="top:373px">ASSESSMENT PROGRESS<span class="pct">60%</span><div class="bar"><span></span></div></div>
    <div class="btn ghost" style="left:10px;width:88px;top:398px;height:20px"><svg width="7" height="7"><use href="#i-left"/></svg>Prev</div>
    <div class="btn primary" style="right:10px;width:88px;top:398px;height:20px">Next<svg width="7" height="7"><use href="#i-right"/></svg></div>
    <div class="home-bar"></div>
  </section>

  <div class="screen-label" style="left:990px;top:1148px">ADD ASSESSMENT - QUESTION - NO</div>
  <section class="screen" style="left:1016px;top:1148px">
    <div class="q-head"></div><div class="q-body"></div>
    <div class="status"><span class="time">9:41</span><span class="icons"><span style="width:8px;height:5px"></span><span style="width:7px;height:5px;border-radius:3px"></span><span style="width:10px;height:5px"></span></span></div>
    <span class="q-kicker">FIRE RISK ASSESSMENT</span><span class="q-title">Fire Hazards</span><span class="q-section"><b>Section 22.5</b> / 30.00</span>
    <span class="save"><i><svg width="9" height="9" style="color:var(--red);margin-top:3.5px"><use href="#i-save"/></svg></i>Save and close</span>
    <span class="topic-ring"><svg width="37" height="37" viewBox="0 0 40 40"><circle cx="20" cy="20" r="17" fill="none" stroke="#1fae3c" stroke-width="2.4"/><use href="#i-bolt" x="11" y="10" width="18" height="20" style="color:var(--amber)"/></svg></span>
    <p class="topic">Electronic Sources of Ignition<small>(Clause 13 &amp; Annex B)</small></p>
    <div class="divider"></div>
    <span class="q-no">QUESTION 22.05</span>
    <p class="q-text">Are reasonable measures taken to prevent fires of electrical origin?</p>
    <div class="answers"><span class="ans yes"><i><svg width="10" height="10" style="color:var(--green)"><use href="#i-tick"/></svg></i>Yes</span><span class="ans no on"><i><svg width="10" height="10" style="color:#fff"><use href="#i-x"/></svg></i>No</span><span class="ans na"><i><svg width="11" height="11" style="color:var(--red)"><use href="#i-ban"/></svg></i>N/A</span></div>
    <div class="note">No, electric sockets are overloaded.</div>
    <span class="more-label" style="top:325px">MORE OPTIONS</span>
    <span class="tool" style="left:10px;width:90px;top:336px"><svg width="7" height="7"><use href="#i-mic"/></svg>Mic</span>
    <span class="tool" style="right:10px;width:90px;top:336px"><svg width="8" height="8"><use href="#i-cam"/></svg>Take a photo</span>
    <div class="progress" style="top:373px">ASSESSMENT PROGRESS<span class="pct">60%</span><div class="bar"><span></span></div></div>
    <div class="btn ghost" style="left:10px;width:88px;top:398px;height:20px"><svg width="7" height="7"><use href="#i-left"/></svg>Prev</div>
    <div class="btn primary" style="right:10px;width:88px;top:398px;height:20px">Next<svg width="7" height="7"><use href="#i-right"/></svg></div>
    <div class="home-bar"></div>
  </section>

  <div class="screen-label" style="left:1269px;top:1148px">ADD ASSESSMENT - QUESTION - ADD PHOTO</div>
  <section class="screen tall" style="left:1295px;top:1148px">
    <div class="q-head"></div><div class="q-body"></div>
    <div class="status"><span class="time">9:41</span><span class="icons"><span style="width:8px;height:5px"></span><span style="width:7px;height:5px;border-radius:3px"></span><span style="width:10px;height:5px"></span></span></div>
    <span class="q-kicker">FIRE RISK ASSESSMENT</span><span class="q-title">Fire Hazards</span><span class="q-section"><b>Section 22.5</b> / 30.00</span>
    <span class="save"><i><svg width="9" height="9" style="color:var(--red);margin-top:3.5px"><use href="#i-save"/></svg></i>Save and close</span>
    <span class="topic-ring"><svg width="37" height="37" viewBox="0 0 40 40"><circle cx="20" cy="20" r="17" fill="none" stroke="#1fae3c" stroke-width="2.4"/><use href="#i-bolt" x="11" y="10" width="18" height="20" style="color:var(--amber)"/></svg></span>
    <p class="topic">Electronic Sources of Ignition<small>(Clause 13 &amp; Annex B)</small></p>
    <div class="divider"></div>
    <span class="q-no">QUESTION 22.05</span>
    <p class="q-text">Are reasonable measures taken to prevent fires of electrical origin?</p>
    <div class="answers"><span class="ans yes"><i><svg width="10" height="10" style="color:var(--green)"><use href="#i-tick"/></svg></i>Yes</span><span class="ans no on"><i><svg width="10" height="10" style="color:#fff"><use href="#i-x"/></svg></i>No</span><span class="ans na"><i><svg width="11" height="11" style="color:var(--red)"><use href="#i-ban"/></svg></i>N/A</span></div>
    <div class="note">No, electric sockets are overloaded.</div>
    <span class="more-label" style="top:325px">MORE OPTIONS</span>
    <span class="tool" style="left:10px;width:90px;top:336px"><svg width="7" height="7"><use href="#i-mic"/></svg>Mic</span>
    <span class="tool" style="right:10px;width:90px;top:336px"><svg width="8" height="8"><use href="#i-cam"/></svg>Take a photo</span>
    <span class="more-label" style="top:373px">PHOTOS</span>
    <div class="photo" role="img" aria-label="Photo of tangled electrical cables and an overloaded extension lead on the floor"><span class="photo-del"></span></div>
    <div class="progress" style="top:620px">ASSESSMENT PROGRESS<span class="pct">60%</span><div class="bar"><span></span></div></div>
    <div class="btn ghost" style="left:10px;width:88px;top:646px;height:20px"><svg width="7" height="7"><use href="#i-left"/></svg>Prev</div>
    <div class="btn primary" style="right:10px;width:88px;top:646px;height:20px">Next<svg width="7" height="7"><use href="#i-right"/></svg></div>
    <div class="home-bar"></div>
  </section>

  <div class="title-mark"><span class="dot"></span>Emberline</div>
  <h1 class="title-text">Fire Risk Assessment App</h1>

</main>
</body>
</html>
```